Business Card Design Project

We need a Business Card for an Mechanical Engineering firm in Singapore. The design should be Modern & Technical looking, yet eye catching.

Our company deals in Cutting Tools & Machine Accessories for the Manufacturing Industries such as Oil & Gas, Aero Space, etc... For more information on our Company, you can either email me or view our website www.valtrion.com.sg.

We are trying to revamp our image to give our consumers a fresh new perspective to our company, so we welcome all ideas.

Industry/Entity Type

Business

Requirements
Must have
• Must incorporate New Company Logo into the card as shown in Uploaded file.

```html
<!DOCTYPE html>
<html lang="en">
<head>
<meta charset="utf-8">
<title>Valtrion Tools – Business Cards</title>
<link rel="stylesheet" href="https://fonts.googleapis.com/css2?family=Lato:wght@400;700&display=swap">
<style>
  :root {
    --bg: #e9e5e0;
    --white: #ffffff;
    --maroon: #7b1533;
    --graphite: #4a4a4a;
    --flame: #ec4322;
    --ink: #1f1f1f;
    --text: #3a3a3a;
    --faint-pink: #fcedf2;
    --faint-grey: #f1f1f1;
  }
  html, body {
    margin: 0;
    padding: 0;
    width: 1200px;
    height: 873px;
    overflow: hidden;
    background: var(--bg);
    font-family: "Lato", sans-serif;
  }
  .sheet { position: relative; width: 1200px; height: 873px; }

  .card {
    position: absolute;
    width: 354px;
    height: 216px;
    border-radius: 19px;
    overflow: hidden;
  }
  .card--back { left: 226px; }
  .card--front { left: 621px; background: var(--white); }
  .row-1 { top: 94px; }
  .row-2 { top: 336px; }
  .row-3 { top: 581px; }

  .card--back.maroon { background: var(--maroon); }
  .card--back.graphite { background: var(--graphite); }
  .card--back.flame { background: var(--flame); }

  /* Brand name lockup */
  .brand {
    position: absolute;
    display: flex;
    align-items: center;
    gap: 7px;
    font-weight: 700;
    letter-spacing: 0.04em;
    text-transform: uppercase;
    white-space: nowrap;
  }
  .brand-dot { border-radius: 50%; flex: none; }
  .card--back .brand {
    left: 50%; top: 50%;
    transform: translate(-50%, -50%);
    color: var(--white);
    font-size: 17px;
  }
  .card--back .brand-dot { width: 14px; height: 14px; background: var(--white); }
  .card--front .brand {
    left: 18px; top: 30px;
    color: var(--maroon);
    font-size: 9px;
    gap: 4px;
  }
  .card--front .brand-dot { width: 8px; height: 8px; background: var(--maroon); }

  /* Faint brand name decoration */
  .watermark {
    position: absolute;
    right: -14px;
    top: 54px;
    font-weight: 700;
    font-size: 64px;
    line-height: 0.9;
    letter-spacing: 0.02em;
    text-align: right;
    text-transform: uppercase;
    color: var(--faint-grey);
    white-space: nowrap;
  }
  .maroon-set .watermark { color: var(--faint-pink); }

  /* Accent bars */
  .accent { position: absolute; width: 9px; }
  .accent--right { right: 0; top: 87px; height: 40px; }
  .accent--left { left: 0; top: 137px; height: 58px; }
  .maroon-set .accent { background: var(--maroon); }
  .graphite-set .accent { background: var(--graphite); }
  .flame-set .accent { background: var(--flame); }

  /* Person */
  .person {
    position: absolute;
    left: 264px;
    top: 88px;
    color: var(--text);
    font-size: 7.5px;
    line-height: 11px;
  }
  .person-name {
    margin: 0 0 1px;
    font-size: 14.5px;
    line-height: 18px;
    font-weight: 400;
    color: var(--ink);
    border-bottom: 1px solid #c9c9c9;
    padding-bottom: 1px;
    width: 72px;
  }
  .person p { margin: 0; }

  /* Company */
  .company {
    position: absolute;
    left: 19px;
    top: 138px;
    font-size: 7.5px;
    line-height: 9.5px;
    color: var(--text);
  }
  .company p { margin: 0; }
  .contact {
    display: grid;
    grid-template-columns: 24px 1px auto;
    column-gap: 4px;
    margin-top: 6px;
    font-size: 6.8px;
    line-height: 8.5px;
  }
  .contact-rule { grid-row: 1 / span 3; grid-column: 2; background: var(--text); }
  .contact .label { grid-column: 1; }
  .contact .value { grid-column: 3; }
</style>
</head>
<body>
<main class="sheet">

  <!-- Row 1 : maroon -->
  <section class="card card--back maroon row-1">
    <div class="brand"><span class="brand-dot"></span>Valtrion Tools</div>
  </section>
  <section class="card card--front maroon-set row-1">
    <div class="watermark" aria-hidden="true">Valtrion<br>Tools</div>
    <div class="brand"><span class="brand-dot"></span>Valtrion Tools</div>
    <span class="accent accent--right"></span>
    <div class="person">
      <h2 class="person-name">Marissa</h2>
      <p>Mob : xxxxxxxxxx</p>
      <p>Email : xxxxxxxxx</p>
    </div>
    <span class="accent accent--left"></span>
    <div class="company">
      <p>Valtrion Tools Pte Ltd</p>
      <p>52 Kallang Way #03-12,</p>
      <p>Kallang Works Hub,</p>
      <p>Singapore 349331</p>
      <div class="contact">
        <span class="contact-rule"></span>
        <span class="label">Tel</span><span class="value">65-61230457</span>
        <span class="label">Fax</span><span class="value">65-61230458</span>
        <span class="label">Email</span><span class="value">info@valtrion.com.sg</span>
      </div>
    </div>
  </section>

  <!-- Row 2 : graphite -->
  <section class="card card--back graphite row-2">
    <div class="brand"><span class="brand-dot"></span>Valtrion Tools</div>
  </section>
  <section class="card card--front graphite-set row-2">
    <div class="watermark" aria-hidden="true">Valtrion<br>Tools</div>
    <div class="brand"><span class="brand-dot"></span>Valtrion Tools</div>
    <span class="accent accent--right"></span>
    <div class="person">
      <h2 class="person-name">Marissa</h2>
      <p>Mob : xxxxxxxxxx</p>
      <p>Email : xxxxxxxxx</p>
    </div>
    <span class="accent accent--left"></span>
    <div class="company">
      <p>Valtrion Tools Pte Ltd</p>
      <p>52 Kallang Way #03-12,</p>
      <p>Kallang Works Hub,</p>
      <p>Singapore 349331</p>
      <div class="contact">
        <span class="contact-rule"></span>
        <span class="label">Tel</span><span class="value">65-61230457</span>
        <span class="label">Fax</span><span class="value">65-61230458</span>
        <span class="label">Email</span><span class="value">info@valtrion.com.sg</span>
      </div>
    </div>
  </section>

  <!-- Row 3 : flame -->
  <section class="card card--back flame row-3">
    <div class="brand"><span class="brand-dot"></span>Valtrion Tools</div>
  </section>
  <section class="card card--front flame-set row-3">
    <div class="watermark" aria-hidden="true">Valtrion<br>Tools</div>
    <div class="brand"><span class="brand-dot"></span>Valtrion Tools</div>
    <span class="accent accent--right"></span>
    <div class="person">
      <h2 class="person-name">Marissa</h2>
      <p>Mob : xxxxxxxxxx</p>
      <p>Email : xxxxxxxxx</p>
    </div>
    <span class="accent accent--left"></span>
    <div class="company">
      <p>Valtrion Tools Pte Ltd</p>
      <p>52 Kallang Way #03-12,</p>
      <p>Kallang Works Hub,</p>
      <p>Singapore 349331</p>
      <div class="contact">
        <span class="contact-rule"></span>
        <span class="label">Tel</span><span class="value">65-61230457</span>
        <span class="label">Fax</span><span class="value">65-61230458</span>
        <span class="label">Email</span><span class="value">info@valtrion.com.sg</span>
      </div>
    </div>
  </section>

</main>
</body>
</html>
```